BrivaTrek Freight Services Business cards

Would like a very unique design catchy but professional for business cards. Please use log provided.Marlon WellsCeo and Founder TransCon Logistix Solutions1-888-913-3225mwells@tlsolutionsus.comwww.bfservicesco.com

```html
<!DOCTYPE html>
<html lang="en">
<head>
<meta charset="utf-8">
<title>BrivaTrek Freight Services – Business Cards</title>
<link rel="stylesheet" href="https://fonts.googleapis.com/css2?family=Questrial&display=swap">
<style>
  :root {
    --brand-blue: #1f73c2;
    --brand-red: #e8262d;
    --card-white: #ffffff;
    --backdrop: #e9eaec;
    --shadow: rgba(0, 0, 0, 0.14);
  }
  * { box-sizing: border-box; margin: 0; padding: 0; }
  html, body {
    width: 1200px;
    height: 576px;
    overflow: hidden;
  }
  body {
    background: var(--backdrop);
    font-family: "Questrial", sans-serif;
    display: flex;
    align-items: center;
    justify-content: center;
    gap: 72px;
  }
  .card {
    position: relative;
    width: 286px;
    height: 500px;
    background: var(--card-white);
    box-shadow: 0 6px 22px var(--shadow);
    overflow: hidden;
  }

  /* ---------- back ---------- */
  .card-back .brand-name {
    position: absolute;
    top: 210px;
    left: 0;
    right: 0;
    text-align: center;
    color: var(--brand-blue);
    font-size: 30px;
    letter-spacing: 0.5px;
  }
  .card-back .website {
    position: absolute;
    bottom: 34px;
    left: 0;
    right: 0;
    text-align: center;
    color: var(--brand-blue);
    font-size: 15px;
    letter-spacing: 0.3px;
  }

  /* ---------- front ---------- */
  .card-front .brand-name {
    position: absolute;
    top: 62px;
    left: 40px;
    color: var(--brand-blue);
    font-size: 26px;
  }
  .edge-tab {
    position: absolute;
    top: 218px;
    width: 14px;
    height: 54px;
  }
  .edge-tab--left { left: 0; }
  .edge-tab--right { right: 0; }

  .identity {
    position: absolute;
    top: 214px;
    left: 30px;
    right: 24px;
  }
  .identity .person-name {
    color: var(--brand-blue);
    font-size: 21px;
    letter-spacing: 0.6px;
    line-height: 1.2;
  }
  .identity .person-title {
    color: var(--brand-blue);
    font-size: 17px;
    line-height: 1.2;
    padding-top: 4px;
    border-top: 1.5px solid var(--brand-red);
    margin-top: 4px;
    width: 150px;
  }
  .identity .company-name {
    color: var(--brand-red);
    font-size: 15px;
    margin-top: 6px;
  }

  .contact-list {
    position: absolute;
    left: 30px;
    bottom: 40px;
    list-style: none;
  }
  .contact-list li {
    display: flex;
    align-items: center;
    gap: 10px;
    color: var(--brand-blue);
    font-size: 15px;
    margin-top: 12px;
  }
  .contact-icon {
    width: 16px;
    height: 16px;
    flex: none;
  }
</style>
</head>
<body>

  <section class="card card-back" aria-label="Business card back">
    <div class="brand-name">BrivaTrek</div>
    <div class="website">www.bfservicesco.com</div>
  </section>

  <section class="card card-front" aria-label="Business card front">
    <div class="brand-name">BrivaTrek</div>

    <svg class="edge-tab edge-tab--left" viewBox="0 0 14 54" aria-hidden="true">
      <rect x="-6" y="0" width="20" height="54" rx="4" fill="var(--brand-blue)"/>
      <rect x="0" y="24" width="14" height="6" fill="var(--brand-red)"/>
    </svg>
    <svg class="edge-tab edge-tab--right" viewBox="0 0 14 54" aria-hidden="true">
      <rect x="0" y="0" width="20" height="54" rx="4" fill="var(--brand-blue)"/>
      <rect x="0" y="24" width="14" height="6" fill="var(--brand-red)"/>
    </svg>

    <div class="identity">
      <div class="person-name">Dustin Harrow</div>
      <div class="person-title">Ceo and Founder</div>
      <div class="company-name">BrivaTrek Freight Services</div>
    </div>

    <ul class="contact-list">
      <li>
        <svg class="contact-icon" viewBox="0 0 16 16" aria-hidden="true">
          <circle cx="8" cy="8" r="8" fill="var(--brand-blue)"/>
          <path d="M5.2 4.3l1.4-.3.8 1.9-.9.7c.4.9 1.1 1.7 2 2.1l.7-.9 1.9.8-.3 1.4c-3 .2-5.8-2.7-5.6-5.7z" fill="#fff"/>
        </svg>
        1-888-472-6081
      </li>
      <li>
        <svg class="contact-icon" viewBox="0 0 16 16" aria-hidden="true">
          <circle cx="8" cy="8" r="8" fill="var(--brand-blue)"/>
          <rect x="4" y="5.2" width="8" height="5.6" fill="#fff"/>
          <path d="M4 5.4l4 3 4-3" fill="none" stroke="var(--brand-blue)" stroke-width="0.9"/>
        </svg>
        dharrow@bfservicesco.com
      </li>
      <li>
        <svg class="contact-icon" viewBox="0 0 16 16" aria-hidden="true">
          <circle cx="8" cy="8" r="8" fill="var(--brand-blue)"/>
          <g fill="none" stroke="#fff" stroke-width="0.9">
            <circle cx="8" cy="8" r="4"/>
            <ellipse cx="8" cy="8" rx="1.8" ry="4"/>
            <path d="M4 8h8"/>
          </g>
        </svg>
        www.bfservicesco.com
      </li>
    </ul>
  </section>

</body>
</html>
```